Quillrun Couriers Web design

Take a look at our existing website(www.qlnrun.com) and design a new one, plus coding and recreate an existing logo.

```html
<!DOCTYPE html>
<html lang="en">
<head>
<meta charset="utf-8">
<title>Quillrun Couriers</title>
<link href="https://fonts.googleapis.com/css2?family=Poppins:wght@300;400;600;700&family=Alegreya+Sans:ital,wght@1,300&display=swap" rel="stylesheet">
<style>
  :root {
    --nav-bg: rgba(32, 36, 42, 0.92);
    --nav-text: #ffffff;
    --accent: #e98a14;
    --hero-dark: #2a3440;
    --hero-mid: #5a6672;
    --hero-warm: #8a5a4e;
    --heading-grey: #5b5b5b;
    --label-dark: #111111;
    --css-blue: #1f78c1;
    --html-orange: #e4502a;
    --js-gold: #e9a824;
    --kit-purple: #6f4ea8;
    --page-bg: #ffffff;
  }
  * { margin: 0; padding: 0; box-sizing: border-box; }
  html, body { width: 1200px; height: 711px; overflow: hidden; background: var(--page-bg); }
  .page { position: relative; width: 1200px; height: 711px; overflow: hidden; font-family: "Poppins", sans-serif; }

  .hero {
    position: absolute; left: 0; top: 0; width: 1200px; height: 444px;
    background:
      radial-gradient(ellipse at 55% 45%, rgba(200,200,205,0.35), transparent 45%),
      linear-gradient(90deg, rgba(138,90,78,0.55) 0%, transparent 35%, transparent 65%, rgba(170,80,50,0.45) 100%),
      linear-gradient(180deg, var(--hero-dark) 0%, var(--hero-mid) 45%, var(--hero-warm) 75%, #3a3f46 100%);
  }
  .nav {
    position: absolute; left: 0; top: 0; width: 1200px; height: 49px;
    background: var(--nav-bg);
  }
  .brand {
    position: absolute; left: 161px; top: 15px;
    font-weight: 600; font-size: 15px; color: var(--nav-text); letter-spacing: 0.3px;
  }
  .menu { position: absolute; top: 17px; left: 0; list-style: none; }
  .menu li {
    position: absolute; white-space: nowrap;
    font-size: 11px; letter-spacing: 1.2px; color: var(--nav-text);
  }
  .menu li.active { color: var(--accent); }
  .menu svg { vertical-align: middle; margin-left: 4px; }

  .play { position: absolute; left: 559px; top: 106px; }
  .hero-title {
    position: absolute; left: 0; top: 200px; width: 1189px; text-align: center;
    font-weight: 300; font-size: 34px; line-height: 38px; color: #ffffff;
  }
  .corner-badge {
    position: absolute; left: 713px; top: 369px; width: 476px; height: 75px;
    background: rgba(60, 64, 70, 0.55);
  }
  .corner-badge span {
    position: absolute; left: 24px; top: 18px;
    font-weight: 600; font-size: 30px; color: #d8d8d8;
  }
  .curl { position: absolute; left: 0; top: 440px; }

  .tech-heading {
    position: absolute; left: 0; top: 476px; width: 1200px; text-align: center;
    font-family: "Alegreya Sans", sans-serif; font-style: italic; font-weight: 300;
    font-size: 36px; color: var(--heading-grey);
  }
  .tech { position: absolute; top: 530px; width: 110px; text-align: center; }
  .tech-label { font-weight: 600; font-size: 27px; line-height: 36px; color: var(--label-dark); }
  .tech-label.kit { font-weight: 400; color: var(--kit-purple); }
  .tech-mark { display: block; margin: 2px auto 0; border-radius: 10px; }
  .tech-shadow {
    display: block; margin: 10px auto 0; width: 90px; height: 14px; border-radius: 50%;
    background: radial-gradient(ellipse, rgba(0,0,0,0.35), transparent 70%);
  }
</style>
</head>
<body>
<div class="page">
  <section class="hero" role="img" aria-label="Photo of a white delivery truck inside a busy warehouse with motion-blurred forklifts"></section>

  <header class="nav">
    <div class="brand">Quillrun Couriers</div>
    <ul class="menu">
      <li class="active" style="left:538px">HOME</li>
      <li style="left:592px">ABOUT US</li>
      <li style="left:671px">SERVICES<svg width="8" height="6" viewBox="0 0 8 6"><path d="M1 1l3 3 3-3" fill="none" stroke="#fff" stroke-width="1.6"/></svg></li>
      <li style="left:762px">RATES</li>
      <li style="left:818px">CUSTOMER BENEFITS</li>
      <li style="left:961px">CONTACT</li>
    </ul>
  </header>

  <svg class="play" width="72" height="72" viewBox="0 0 72 72" aria-label="Play video">
    <circle cx="36" cy="36" r="34" fill="none" stroke="#fff" stroke-width="2"/>
    <path d="M27 21 L54 36 L27 51 Z" fill="#fff"/>
  </svg>
  <h1 class="hero-title">View Our Services By Watching<br>This Short Video</h1>

  <div class="corner-badge"><span>Quillrun Couriers</span></div>

  <svg class="curl" width="1200" height="34" viewBox="0 0 1200 34">
    <defs>
      <linearGradient id="curlShade" x1="0" y1="0" x2="0" y2="1">
        <stop offset="0" stop-color="#000" stop-opacity="0.45"/>
        <stop offset="1" stop-color="#000" stop-opacity="0"/>
      </linearGradient>
    </defs>
    <path d="M22 4 L1170 4 L1168 30 Q600 14 26 30 Z" fill="url(#curlShade)"/>
  </svg>

  <h2 class="tech-heading">Your website will be coded with this technology.</h2>

  <div class="tech" style="left:344px">
    <div class="tech-label">CSS</div>
    <svg class="tech-mark" width="86" height="98"><rect width="86" height="98" rx="10" fill="var(--css-blue)"/></svg>
    <span class="tech-shadow"></span>
  </div>
  <div class="tech" style="left:457px">
    <div class="tech-label">HTML</div>
    <svg class="tech-mark" width="86" height="98"><rect width="86" height="98" rx="10" fill="var(--html-orange)"/></svg>
    <span class="tech-shadow"></span>
  </div>
  <div class="tech" style="left:567px">
    <div class="tech-label">JS</div>
    <svg class="tech-mark" width="86" height="98"><rect width="86" height="98" rx="10" fill="var(--js-gold)"/></svg>
    <span class="tech-shadow"></span>
  </div>
  <div class="tech" style="left:704px;width:140px">
    <div class="tech-label kit">Strapkit</div>
    <svg class="tech-mark" width="120" height="98"><rect width="120" height="98" rx="14" fill="var(--kit-purple)"/></svg>
    <span class="tech-shadow"></span>
  </div>
</div>
</body>
</html>
```